Bus Bench Ad Design Needed

Hi there. We would like to design an eye catching bus bench ad! The information that we would like to have on it is found below:

- Our logo which is attached below. We would this to take up at least half of the bus bench.
- Our phone number in bold, very visible to see. 813-562-0947. White numbers on an eye catching colored background.
- Our web address : www.SplitEase247.example
- A "Ring Gary" phrase in a black circle with yellow bold letters. Want the "Ring Gary" to be somewhat angled. We are thinking that the "Ring Gary" should be directly below the image in our logo.
- Our tag line we want somewhere in here as well which is "Divorce made easy - at a price you'll like!"

```html
<!DOCTYPE html>
<html lang="en">
<head>
<meta charset="utf-8">
<title>SplitEase Bus Bench Ad</title>
<link rel="stylesheet" href="https://fonts.googleapis.com/css2?family=Open+Sans:wght@400;600;800&family=Questrial&family=Great+Vibes&family=Patua+One&display=swap">
<style>
  :root {
    --brand-blue: #0a7fc6;
    --swoosh-grey: #9a9a9a;
    --panel-dark: #333335;
    --paper: #ffffff;
    --ink: #111111;
    --badge-yellow: #ffe21a;
    --backdrop-light: #8a8a8a;
    --backdrop-dark: #2e2e2e;
  }
  html, body {
    margin: 0;
    padding: 0;
    width: 1200px;
    height: 1200px;
    overflow: hidden;
  }
  body {
    background: linear-gradient(135deg, var(--backdrop-light) 0%, #555 45%, var(--backdrop-dark) 100%);
    display: flex;
    align-items: center;
    justify-content: center;
  }
  .bench-ad {
    width: 1000px;
    height: 250px;
    box-shadow: 0 8px 22px rgba(0,0,0,0.45);
  }
  .bench-ad svg { display: block; width: 100%; height: 100%; }
  .brand-name {
    font-family: "Questrial", sans-serif;
    font-size: 62px;
    letter-spacing: 3px;
    fill: var(--brand-blue);
  }
  .brand-descriptor {
    font-family: "Questrial", sans-serif;
    font-size: 23px;
    fill: var(--ink);
  }
  .phone-number {
    font-family: "Open Sans", sans-serif;
    font-weight: 800;
    font-size: 78px;
    fill: var(--paper);
  }
  .tagline {
    font-family: "Great Vibes", cursive;
    font-size: 44px;
    fill: var(--paper);
  }
  .web-address {
    font-family: "Open Sans", sans-serif;
    font-weight: 400;
    font-size: 22px;
    fill: var(--paper);
  }
  .web-address .accent { fill: var(--brand-blue); font-weight: 600; }
  .web-address .bold { font-weight: 600; }
  .badge-text {
    font-family: "Patua One", serif;
    font-size: 26px;
    fill: var(--badge-yellow);
  }
  .brand-blue { fill: var(--brand-blue); }
  .swoosh { fill: var(--swoosh-grey); }
  .panel-dark { fill: var(--panel-dark); }
  .paper { fill: var(--paper); }
  .badge-disc { fill: var(--ink); }
  .badge-ring { fill: none; stroke: var(--badge-yellow); stroke-width: 1; }
  .badge-icon { fill: #2a2a2a; }
</style>
</head>
<body>
  <div class="bench-ad">
    <svg viewBox="0 0 1000 250" xmlns="http://www.w3.org/2000/svg">
      <!-- base -->
      <rect class="paper" x="0" y="0" width="1000" height="250"/>

      <!-- dark lower-right panel -->
      <rect class="panel-dark" x="600" y="140" width="400" height="110"/>

      <!-- grey swoosh divider -->
      <path class="swoosh" d="M585 0 L625 0 C600 40 592 90 600 150 C608 200 625 230 634 250 L600 250 C590 220 572 170 573 110 C574 60 578 25 585 0 Z"/>

      <!-- blue upper-right panel -->
      <path class="brand-blue" d="M612 0 L1000 0 L1000 153 C900 170 760 180 645 172 C610 140 598 80 612 0 Z"/>

      <!-- blue lower-left band -->
      <path class="brand-blue" d="M0 155 C120 140 260 135 360 138 C460 141 540 145 590 150 C592 195 605 228 620 250 L0 250 Z"/>

      <!-- brand name -->
      <circle class="brand-blue" cx="82" cy="68" r="30"/>
      <text class="brand-name" x="135" y="85">SPLITEASE</text>
      <text class="brand-descriptor" x="138" y="116" textLength="405">Non-Lawyer Documents Service</text>

      <!-- phone -->
      <text class="phone-number" x="60" y="226" textLength="490" lengthAdjust="spacingAndGlyphs">813-562-0947</text>

      <!-- speech badge -->
      <g class="ring-badge">
        <path class="badge-disc" d="M574 180 C566 195 556 203 545 207 C565 206 580 200 592 192 Z"/>
        <circle class="badge-disc" cx="602" cy="154" r="47"/>
        <circle class="badge-ring" cx="602" cy="154" r="43"/>
        <path class="badge-icon" d="M586 126 c6 -3 12 -2 14 3 l4 10 c1 4 -1 7 -4 8 l-4 2 c2 8 6 14 12 19 l3 -3 c3 -2 7 -2 9 1 l6 9 c2 4 1 9 -3 11 c-20 6 -44 -26 -37 -60 Z"/>
        <g transform="rotate(-16 602 154)">
          <text class="badge-text" x="602" y="150" text-anchor="middle">Ring</text>
          <text class="badge-text" x="604" y="176" text-anchor="middle">Gary</text>
        </g>
      </g>

      <!-- tagline -->
      <text class="tagline" x="667" y="66">Divorce made easy –</text>
      <text class="tagline" x="667" y="108">at a price</text>
      <text class="tagline" x="718" y="143">you'll like!</text>

      <!-- web address -->
      <text class="web-address" x="665" y="213" textLength="300" lengthAdjust="spacingAndGlyphs">www.<tspan class="accent">SplitEase</tspan><tspan class="bold">247</tspan>.example</text>
    </svg>
  </div>
</body>
</html>
```